ポーカーイベントでのポスターデザインの制作依頼です。 【 依頼内容】 ・イメージポスター画像のように"赤"を基調としたデザインとして仕上げてください。 ・必須情報として、 ①『KRX Season 15』→これはタイトルの位置付け。上に配置。 ③『日程』→2025.12.11 - 14 ④『会場』→難波 楓坂ホール b2 hall ⑤『プライズ』Event Total Prize 総額5,000万円or50,000,000円 ⑥補足『西日本を制せ』がキャッチコピーなのでインパクトを持たせて配置してください。 <サイズ> ・A1 ポスターサイズ 【 デザインイメージ 】 https://sheets.plavencloud.net/d/7qR2kLmZ8vTyX4wNc0bHs1DfGpJ6eUoAiQ3zVxYtKl9M/edit?gid=0#gid=0 【 Webページ 】 https://veltrashgames.com/ URL内に デザインイメージ(依頼はポスター画像です) 赤基調でお願いします。 【 契約金額(税抜) 】 3万円 ご応募をお待ちしております! |
| https://sheets.plavencloud.net/d/7qR2kLmZ8vTyX4wNc0bHs1DfGpJ6eUoAiQ3zVxYtKl9M/edit?gid=0#gid=0 | ||

```html
<!DOCTYPE html>
<html lang="ja">
<head>
<meta charset="UTF-8">
<title>KRX Season 15 — 西日本を制せ。</title>
<link rel="stylesheet" href="https://fonts.googleapis.com/css2?family=Anton&family=Dela+Gothic+One&family=Noto+Sans+JP:wght@700;900&family=Roboto+Condensed:ital,wght@1,800;1,900&display=swap">
<style>
  :root {
    --red: #d8141c;
    --red-deep: #9e0a10;
    --red-pale: #f05a5a;
    --ink: #111111;
    --white: #ffffff;
  }
  * { margin: 0; padding: 0; box-sizing: border-box; }
  html, body { width: 848px; height: 1200px; overflow: hidden; background: var(--red); }
  .poster {
    position: relative; width: 848px; height: 1200px; overflow: hidden;
    background:
      linear-gradient(115deg, transparent 0 52%, rgba(255,255,255,.08) 52% 56%, transparent 56% 70%, rgba(255,255,255,.06) 70% 72%, transparent 72%),
      radial-gradient(ellipse at 60% 60%, var(--red) 0%, var(--red-deep) 100%);
    font-family: "Noto Sans JP", sans-serif; color: var(--white);
  }
  .crowd-photo {
    position: absolute; left: 0; top: 0; width: 848px; height: 330px;
    background: linear-gradient(180deg, #4a3a3c 0%, #6b3034 55%, rgba(216,20,28,0) 100%);
  }
  .event-mark {
    position: absolute; left: -10px; top: -60px; width: 870px;
    font-family: "Anton", sans-serif; font-size: 320px; line-height: 1;
    letter-spacing: 10px; text-align: center;
    color: rgba(240,90,90,.45); -webkit-text-stroke: 3px rgba(255,255,255,.45);
  }
  .player-photo {
    position: absolute; left: 0; top: 200px; width: 420px; height: 760px;
    background: radial-gradient(ellipse at 45% 45%, #5a3f3a 0%, #2c1d1e 55%, rgba(44,29,30,0) 75%);
  }
  .season {
    position: absolute; left: 315px; top: 138px;
    font-family: "Roboto Condensed", sans-serif; font-style: italic; font-weight: 900;
    font-size: 84px; line-height: 1; color: var(--ink); letter-spacing: -1px;
    -webkit-text-stroke: 2px var(--white); paint-order: stroke fill;
  }
  .date {
    position: absolute; left: 345px; top: 236px;
    font-family: "Roboto Condensed", sans-serif; font-style: italic; font-weight: 800;
    font-size: 54px; line-height: 1; letter-spacing: 1px;
  }
  .venue {
    position: absolute; left: 347px; top: 298px; font-weight: 900; font-size: 36px; line-height: 1; letter-spacing: 1px;
  }
  .catch { position: absolute; font-family: "Dela Gothic One", sans-serif; line-height: 1; font-size: 128px; letter-spacing: -4px; }
  .catch-band {
    display: inline-block; background: var(--ink); transform: skewY(-6deg); padding: 10px 18px 18px;
  }
  .catch-top { left: 20px; top: 440px; }
  .catch-bottom { left: 390px; top: 620px; }
  .catch-en {
    position: absolute; left: 650px; top: 470px; font-family: "Roboto Condensed", sans-serif;
    font-style: italic; font-weight: 800; font-size: 20px; line-height: 1.15; color: var(--white);
  }
  .prize-label {
    position: absolute; left: 200px; top: 852px; font-family: "Roboto Condensed", sans-serif;
    font-style: italic; font-weight: 800; font-size: 44px; line-height: 1; transform: rotate(-4deg);
  }
  .prize-total {
    position: absolute; left: 48px; top: 965px; width: 66px; height: 200px;
    background: var(--ink); display: flex; flex-direction: column; align-items: center; justify-content: center;
    font-weight: 900; font-size: 54px; line-height: 1.2;
  }
  .prize-amount {
    position: absolute; left: 130px; top: 925px; font-family: "Anton", sans-serif;
    font-size: 255px; line-height: 1; letter-spacing: -2px; transform: skewX(-6deg);
  }
  .prize-unit {
    position: absolute; left: 690px; top: 900px; font-weight: 900; font-size: 58px; line-height: 1; color: var(--white);
  }
  .brand {
    position: absolute; right: 20px; bottom: 30px; width: 130px;
    display: flex; flex-direction: column; align-items: center; gap: 10px;
  }
  .brand-square { width: 48px; height: 48px; background: var(--white); }
  .brand-name { font-weight: 700; font-size: 15px; line-height: 1; white-space: nowrap; color: var(--white); }
</style>
</head>
<body>
<main class="poster">
  <div class="crowd-photo" role="img" aria-label="ポーカートーナメント会場でプレイヤーがテーブルを囲む写真"></div>
  <div class="event-mark" aria-hidden="true">KRX</div>
  <div class="player-photo" role="img" aria-label="拳を握りしめて気合いを入れるポーカープレイヤーの写真"></div>

  <h1 class="season">Season 15</h1>
  <p class="date">2025.12.11-14</p>
  <p class="venue">難波 楓坂ホール b2 hall</p>

  <p class="catch catch-top"><span class="catch-band">西日本を</span></p>
  <p class="catch catch-bottom"><span class="catch-band">制せ。</span></p>
  <p class="catch-en">Conquer<br>the West.</p>

  <p class="prize-label">Event Total Prize</p>
  <div class="prize-total"><span>総</span><span>額</span></div>
  <p class="prize-amount">5,000</p>
  <p class="prize-unit">万円</p>

  <div class="brand">
    <span class="brand-square"></span>
    <span class="brand-name">Veltrash Games</span>
  </div>
</main>
</body>
</html>
```